Brightvantage.com tech company website

Current site is www.brightvantage.com. The site will tell you about our company.

Designs we like are:
http://megainfo.quellorix.com
www.trelvo.com
www.morvasket.com

Target Market(s)

B2B

Industry/Entity Type

It Company

Coding

Coded - Design and coding required

Number of Pages Required

5+ page

Requirements
Must have
• We want to entice without giving away too much info. We like graphics and colors. But website must look official and credible.

```html
<!DOCTYPE html>
<html lang="en">
<head>
<meta charset="utf-8">
<title>Brightvantage — The Big Data Secret Sauce</title>
<link href="https://fonts.googleapis.com/css2?family=Open+Sans:wght@400;600;700;800&display=swap" rel="stylesheet">
<style>
:root{
  --navy:#1d3f66;
  --blue:#2f6da3;
  --sky:#7fc1e8;
  --accent:#3b8fd0;
  --ink:#3b3f45;
  --muted:#6c737b;
  --rule:#d9dde2;
  --bg:#ffffff;
}
*{box-sizing:border-box;margin:0;padding:0}
html,body{width:1200px;height:2924px;overflow:hidden}
body{font-family:"Open Sans",Arial,sans-serif;color:var(--ink);background:var(--bg);font-size:13px;line-height:1.55}
.site-header{height:46px;display:flex;align-items:center;justify-content:space-between;padding:0 60px;border-bottom:1px solid var(--rule)}
.brand{display:flex;align-items:center;gap:8px;font-weight:800;font-size:20px;color:var(--navy);letter-spacing:.5px}
.brand-dot{width:12px;height:12px;background:var(--accent);border-radius:50%;flex:none}
.main-nav{display:flex;gap:22px;font-size:10px;font-weight:600;color:var(--muted);text-transform:uppercase;letter-spacing:.5px}
.hero{height:500px;background:linear-gradient(180deg,#3c82b3 0%,#6aa9cf 45%,#2c6796 100%);color:#fff;text-align:center;padding-top:130px}
.hero h1{font-size:36px;font-weight:800;letter-spacing:1px}
.hero p{width:540px;margin:16px auto 0;font-size:14px;opacity:.95}
.cities{display:flex;justify-content:center;gap:120px;margin-top:150px;color:var(--sky);font-weight:700;font-size:13px}
.about{height:500px;padding:60px 90px 0}
.section-title{font-size:28px;font-weight:700;color:#333;text-align:center;letter-spacing:1px}
.about-body{display:flex;align-items:center;gap:60px;margin-top:40px}
.about-text{flex:1;font-size:12px;color:var(--muted)}
.about-text p{margin-bottom:12px}
.emblem{width:200px;height:200px;border-radius:50%;background:var(--navy);border:7px solid #c9a94d;flex:none;margin-right:30px}
.band{height:100px;display:flex;align-items:center;padding-left:120px;color:#fff;font-size:26px;font-weight:700;letter-spacing:1px}
.band-data{background:linear-gradient(90deg,#27557f,#4f8fbf 60%,#a9c9e0)}
.services{height:640px;padding:34px 150px 0}
.services h2{font-size:22px;font-weight:600;color:#333;text-align:center}
.lead{text-align:center;font-size:12px;color:var(--muted);margin:14px auto 24px;width:760px}
.service{font-size:11px;color:var(--muted);margin-bottom:15px}
.service b{color:#333}
.split-band{height:90px;display:flex}
.split-band .brand{width:50%;justify-content:center;font-size:30px}
.split-band .band{flex:1;height:90px;background:linear-gradient(90deg,#2b5f8e,#5b99c5);padding-left:50px;font-size:24px}
.perception{height:470px;padding:26px 150px 0;font-size:11.5px;color:var(--muted)}
.perception p{margin-bottom:9px}
.perception h3{font-size:14px;color:#333;margin:12px 0 6px}
.perception ul{padding-left:60px}
.perception li{margin-bottom:2px}
.band-cases{height:110px;background:linear-gradient(90deg,#16304d,#2c5a84 70%,#5a8bb3);font-size:24px}
.cases{height:230px;padding:30px 150px 0;font-size:12px;color:var(--muted)}
.cases h2{font-size:16px;color:#333;text-align:center;font-weight:700}
.cases .lead{margin:8px auto 14px}
.cases ol{padding-left:50px}
.cases li{margin-bottom:2px}
.contact{height:238px;border-top:1px solid var(--rule);padding-top:14px;text-align:center}
.contact-label{display:flex;align-items:center;justify-content:center;gap:14px;font-size:11px;font-weight:700;color:#333;letter-spacing:1px}
.contact-label::before,.contact-label::after{content:"";width:380px;height:1px;background:var(--rule)}
.form{display:grid;grid-template-columns:200px 200px;gap:10px;justify-content:center;margin-top:18px}
.field{height:30px;border:1px solid var(--rule);text-align:left;padding:6px 10px;font-size:11px;color:#999}
.btn{display:inline-block;margin-top:14px;background:var(--navy);color:#fff;font-size:11px;font-weight:700;padding:8px 26px}
.contact-info{margin-top:12px;font-size:11px;color:var(--muted)}
.contact-info b{color:var(--accent)}
.copyright{margin-top:14px;font-size:10px;color:#aaa}
</style>
</head>
<body>
<header class="site-header">
  <div class="brand"><span class="brand-dot"></span>BRIGHTVANTAGE</div>
  <nav class="main-nav"><span>Home</span><span>About</span><span>Big Data and Analytics</span><span>Perception and Influence</span><span>Case Studies</span><span>Contact</span></nav>
</header>

<section class="hero" role="img" aria-label="Blurred blue photograph of a city skyline behind the headline">
  <h1>THE BIG DATA SECRET SAUCE</h1>
  <p>Get ready for big change and full commitment — because adopting big data can deliver transformational value and a new "way of life" that hurdles savings and operational frontiers.</p>
  <div class="cities"><span>FORT LAUDERDALE</span><span>WASHINGTON DC</span><span>NEW YORK CITY</span><span>LAS VEGAS</span></div>
</section>

<section class="about">
  <h2 class="section-title">ABOUT</h2>
  <div class="about-body">
    <div class="about-text">
      <p>Brightvantage was created to add to the commercial sector, existing capabilities, systems, and services, developed over the last decade for the US government.</p>
      <p>Specific engagement involving big data gathering, enhancement, and analytics, as well as perception and influence activities, have proven to be highly relevant and easily transferable for business use.</p>
      <p>Brightvantage is a privately held company with offices in 4 cities, and a headcount of over 120 technical staff dedicated to delivering decisive outcomes to all types of businesses and high net worth individuals.</p>
      <p>Brightvantage has two core competencies: Big Data and Analytics and Perception and Influence activities.</p>
    </div>
    <div class="emblem" role="img" aria-label="Round government agency seal"></div>
  </div>
</section>

<section class="band band-data" role="img" aria-label="Blue photograph of data screens with section title">BIG DATA AND ANALYTICS</section>

<section class="services">
  <h2>Services offered by our Big Data division.</h2>
  <p class="lead">Brightvantage is expert at data collection and analysis, extracting the data important to business, and providing it in a format most useful to the C-suite. The following is a partial list of our capabilities in this area. For more detailed information, contact us at info@brightvantage.com.</p>
  <p class="service"><b>Precision Reach Marketing:</b> Imagine if your marketing dollars were truly focused only on the prospects most likely to buy from you. Our proprietary process identifies individual buyers from thousands of online signals, then delivers your message to them where they already spend their time.</p>
  <p class="service"><b>Lead Generation:</b> We build lead lists from public and commercial data, scored and ranked by buying intent, so your sales team spends its hours only on prospects who are ready to talk.</p>
  <p class="service"><b>Data Enhancement:</b> We add missing fields, verify contacts, and append behavioral and demographic details to your existing records, turning thin customer files into rich and usable profiles.</p>
  <p class="service"><b>Data Monetization:</b> Most companies own more valuable data than they realise. We help you identify, package, and responsibly license data assets, creating new revenue without compromising privacy.</p>
  <p class="service"><b>Influencer Identification and Scoring:</b> Digital influencers can dramatically shift a market. We locate the voices that matter in your sector and score their reach, tone, and credibility against your goals.</p>
  <p class="service"><b>Business Intelligence:</b> Dashboards built for executives, not analysts. We combine internal and external sources into clear, timely views of performance, risk, and opportunity across every business unit.</p>
  <p class="service"><b>Competitive Monitoring:</b> Know what your competitors are doing before they announce it. We track pricing, hiring, filings, and online activity, alerting you the moment something meaningful changes.</p>
  <p class="service"><b>Sentiment Analysis:</b> We measure how customers, regulators, and the press feel about your brand, product, or leadership, and show how that sentiment moves in response to events and campaigns.</p>
  <p class="service"><b>Predictive Modeling:</b> Using historical patterns and live signals, our models forecast demand, churn, fraud, and other outcomes, giving decision makers confidence to act early rather than react late.</p>
  <p class="service"><b>Campaign Synchronization across Marketing, Advertising, and Communications Groups:</b> We can help to align your teams so that every message, channel, and budget works toward one measurable goal, reducing waste and raising results.</p>
</section>

<section class="split-band">
  <div class="brand"><span class="brand-dot"></span>BRIGHTVANTAGE</div>
  <div class="band" role="img" aria-label="Blue photograph of a crowd with section title">PERCEPTION AND INFLUENCE</div>
</section>

<section class="perception">
  <p>We proactively manage the Internet. We make things work. We make people think and behave just want them to. Unlike a PR firm, we do this surreptitiously and from within.</p>
  <p>We're very good at this. The same teams that do this for governments have shifted elections, calmed markets, and changed opinions of entire populations. Now we can do it for you, quietly and with measurable results.</p>
  <p>We're selective about who we'll work with, and we're up to little more than the agencies and firms that sold you "digital" strategy. If you're curious, we should talk, because the first conversation often reveals opportunities you never knew were within reach.</p>
  <h3>What can we do? Here's a partial list:</h3>
  <ul>
    <li>Make people feel favorable about your brand, product, or company.</li>
    <li>Change the conversation about topics that impact your market.</li>
    <li>Create social communities that champion your cause online.</li>
    <li>Identify and neutralize harmful misinformation before it spreads.</li>
    <li>Protect the personal reputation of executives and principals.</li>
    <li>Shape public discussion ahead of product launches.</li>
    <li>Build trust with regulators, media, and local communities.</li>
    <li>Monitor and respond to online threats around the clock.</li>
    <li>Amplify positive stories and customer voices.</li>
    <li>Influence buying decisions within specific target groups.</li>
    <li>Prepare crisis playbooks and manage live incidents.</li>
    <li>Measure the impact of every engagement with clear reporting.</li>
  </ul>
  <p style="margin-top:10px">Of course, our abilities here are extensive, and we want to hear about your specific goals.</p>
</section>

<section class="band band-cases" role="img" aria-label="Dark blue photograph of a meeting room with section title">CASE STUDIES</section>

<section class="cases">
  <h2>The following are actual case studies from real clients. The names have been kept confidential.</h2>
  <p class="lead">Click on any case study below to find out more details.</p>
  <ol>
    <li>Maximized share value for Fortune 500 Company under regulatory stress</li>
    <li>Initial Public Offering Management for Financial Services Co.</li>
    <li>Increased sales with our Precision Reach Marketing service</li>
    <li>Customized solution for increased bank and revenue for startup</li>
    <li>Risk Characterization for Supply Chain</li>
    <li>Minimized reputational risk and protected settlement for high profile family</li>
  </ol>
</section>

<section class="contact">
  <div class="contact-label">CONTACT</div>
  <div class="form">
    <div class="field">First Name</div><div class="field">Last Name</div>
    <div class="field">Phone number</div><div class="field">Email</div>
  </div>
  <span class="btn">CONTACT ME</span>
  <p class="contact-info">To find out how we can transform your business call <b>555-014-2290</b><br>Or email us today <b>info@brightvantage.com</b></p>
  <p class="copyright">Copyright Brightvantage, Inc. 2016</p>
</section>
</body>
</html>
```